Technology Enablement - One Pager

I need (2) one pager piece of marketing collateral to use as outreach for a service offering. The one pager must have a strong call to action, highlight the pain points the service solves.

```html
<!DOCTYPE html>
<html lang="en">
<head>
<meta charset="utf-8">
<title>Technology Enablement – SMB One Pager</title>
<link rel="stylesheet" href="https://fonts.googleapis.com/css2?family=Montserrat:wght@400;500;600;700;800&display=swap">
<style>
  :root{
    --navy:#0b2f5c;
    --yellow:#fdd15a;
    --olive:#7a8464;
    --ink:#1b1b1b;
    --white:#ffffff;
    --page-bg:#e4e4e4;
    --photo-a:#8fa6bf;
    --photo-b:#3d5a7a;
  }
  *{box-sizing:border-box;margin:0;padding:0}
  html,body{width:1200px;height:1200px;overflow:hidden;background:var(--page-bg);font-family:"Montserrat",sans-serif}
  .canvas{position:relative;width:1200px;height:1200px}
  .flyer{position:absolute;left:176px;top:0;width:1198px;height:1694px;background:var(--white);transform:scale(0.7084);transform-origin:0 0;color:var(--ink)}
  .shapes{position:absolute;left:0;top:0}
  .block{position:absolute}
  h1,h2,h3{font-weight:700;color:var(--navy);line-height:1.1}
  .title{font-size:30px}
  .section-title{font-size:30px}
  .on-navy h2{color:var(--yellow)}
  .on-navy{color:var(--white)}
  p{font-size:15.5px;line-height:1.25}
  .gap{margin-top:9px}
  ul{list-style:none}
  li{font-size:15.5px;line-height:22px;position:relative;padding-left:18px}
  .dot li{line-height:19.5px}
  .dot li::before{content:"";position:absolute;left:2px;top:5px;width:11px;height:11px;border:1.5px solid var(--navy);border-radius:50%}
  .dot li::after{content:"";position:absolute;left:5.5px;top:8.5px;width:4px;height:4px;background:var(--navy);border-radius:50%}
  .tick li::before{content:"";position:absolute;left:1px;top:5px;width:12px;height:12px;border:1.3px solid currentColor;border-radius:50%}
  .tick li::after{content:"";position:absolute;left:5px;top:7.5px;width:3px;height:5.5px;border:solid currentColor;border-width:0 1.4px 1.4px 0;transform:rotate(40deg)}
  .tick.yellow li::before,.tick.yellow li::after{border-color:var(--yellow)}
  .tick.navy li::before,.tick.navy li::after{border-color:var(--navy)}
  .box li::before{content:"";position:absolute;left:1px;top:6px;width:11px;height:11px;border:1.3px solid var(--white)}
  .box li::after{content:"";position:absolute;left:4.5px;top:7.5px;width:3px;height:6px;border:solid var(--white);border-width:0 1.4px 1.4px 0;transform:rotate(40deg)}
  .filled li{line-height:19.5px}
  .filled li::before{content:"";position:absolute;left:1px;top:4px;width:12px;height:12px;background:var(--navy)}
  .filled li::after{content:"";position:absolute;left:5px;top:5.5px;width:3px;height:6px;border:solid var(--white);border-width:0 1.5px 1.5px 0;transform:rotate(40deg)}
  .highlight{color:var(--yellow);font-weight:700}
  .cta-lines{position:absolute;left:0;top:1508px;width:1198px;text-align:center;font-size:23px;line-height:29px;color:var(--ink)}
  .cta-button{position:absolute;left:175px;top:1592px;width:849px;height:68px;border-radius:34px;background:var(--navy);color:var(--yellow);font-weight:700;font-size:27px;display:flex;align-items:center;justify-content:center;letter-spacing:0.2px}
</style>
</head>
<body>
<div class="canvas">
  <div class="flyer">
    <svg class="shapes" width="1198" height="1694" viewBox="0 0 1198 1694">
      <!-- top-right frame -->
      <polygon points="980,34 1198,34 1198,208" fill="var(--yellow)"/>
      <polygon points="752,258 752,434 970,434" fill="var(--yellow)"/>
      <rect x="1016" y="56" width="158" height="20" fill="var(--olive)"/>
      <rect x="1154" y="56" width="20" height="120" fill="var(--olive)"/>
      <rect x="776" y="300" width="20" height="112" fill="var(--olive)"/>
      <rect x="776" y="392" width="180" height="20" fill="var(--olive)"/>
      <rect x="782" y="67" width="384" height="337" fill="none" stroke="var(--yellow)" stroke-width="5"/>
      <!-- navy bands -->
      <rect x="0" y="434" width="1198" height="342" fill="var(--navy)"/>
      <polygon points="535,434 587,434 698,605 587,776 535,776 646,605" fill="var(--yellow)"/>
      <rect x="0" y="1256" width="1198" height="234" fill="var(--navy)"/>
      <polygon points="430,1256 466,1256 540,1373 466,1490 430,1490 503,1373" fill="var(--yellow)"/>
      <!-- bottom-left frame -->
      <polygon points="272,776 535,776 535,987" fill="var(--yellow)"/>
      <polygon points="0,1045 0,1256 262,1256" fill="var(--yellow)"/>
      <rect x="300" y="800" width="206" height="20" fill="var(--olive)"/>
      <rect x="486" y="800" width="20" height="160" fill="var(--olive)"/>
      <rect x="30" y="1080" width="20" height="150" fill="var(--olive)"/>
      <rect x="30" y="1210" width="190" height="20" fill="var(--olive)"/>
      <rect x="37" y="815" width="457" height="402" fill="none" stroke="var(--yellow)" stroke-width="5"/>
      <defs>
        <linearGradient id="photoTone" x1="0" y1="0" x2="1" y2="1">
          <stop offset="0" stop-color="var(--photo-a)"/>
          <stop offset="1" stop-color="var(--photo-b)"/>
        </linearGradient>
      </defs>
      <rect x="785" y="70" width="378" height="331" fill="url(#photoTone)" role="img" aria-label="Photo of a smiling professional in a bright office with colleagues and holographic code overlay"/>
      <rect x="40" y="818" width="451" height="396" fill="url(#photoTone)" role="img" aria-label="Photo of a person pointing at a dashboard on a tablet in an office"/>
    </svg>

    <div class="block" style="left:34px;top:44px;width:720px">
      <h1 class="title">Technology Enablement – SMB</h1>
      <p style="margin-top:6px">Your technology shouldn’t slow your business down.<br>We help SMBs turn disconnected tools into systems that actually work.</p>
      <h2 class="section-title" style="margin-top:5px">The Problem</h2>
      <p style="margin-top:5px">Most growing businesses have plenty of software — but no real system.</p>
      <p class="gap">You’ve invested in cloud tools, CRMs, accounting platforms, HR apps, and automation.<br>Yet day-to-day work still feels harder than it should.</p>
      <p class="gap">Common pain points</p>
      <ul class="dot" style="margin-top:5px">
        <li>Software doesn’t talk to each other</li>
        <li>Key processes live in people’s heads</li>
        <li>Manual work fills the gaps between systems</li>
        <li>Decisions are made without clear data</li>
        <li>Tech choices are made reactively, not strategically</li>
      </ul>
      <p class="gap">The result?<br>More effort, more admin, and less return on your software spend.</p>
    </div>

    <div class="block on-navy" style="left:34px;top:460px;width:520px">
      <h2 class="section-title" style="margin-left:24px">What We Do</h2>
      <p style="margin-top:20px">Technology Enablement is about improving how work<br>actually flows through your business.</p>
      <p class="highlight" style="margin-top:14px">Brightlane helps you:</p>
      <ul class="tick yellow" style="margin-top:11px">
        <li>Identify workflow and process gaps</li>
        <li>Find where technology is creating friction (not value)</li>
        <li>Improve adoption of the tools you already pay for</li>
        <li>Clarify where automation and integration will actually help</li>
        <li>Build a practical roadmap tied to real business outcomes</li>
      </ul>
      <p style="margin-top:12px">This is not IT support.<br>It’s operational improvement, using technology as the lever.</p>
    </div>

    <div class="block on-navy" style="left:753px;top:460px;width:430px">
      <h2 class="section-title">Our Approach Is Different</h2>
      <ul class="tick yellow" style="margin-top:18px;padding-left:4px">
        <li>You do not need to switch IT providers</li>
        <li>You do not need to rip and replace systems</li>
        <li>You do not need a long-term contract</li>
      </ul>
      <p style="margin-top:12px">We start with clarity first.<br>Execution comes later — only where it<br>makes sense.</p>
    </div>

    <div class="block" style="left:640px;top:780px;width:550px">
      <h2 class="section-title">Product 1: Technology Enablement Assessment</h2>
      <p style="margin-top:14px">A 2–4 week, stand-alone engagement</p>
      <p class="gap">We assess your:</p>
      <ul class="tick navy" style="margin-top:8px">
        <li>Technology &amp; digital maturity</li>
        <li>Core workflows and handoffs</li>
        <li>Integration and automation opportunities</li>
        <li>Adoption gaps and training needs</li>
        <li>Data, reporting, and KPI visibility</li>
        <li>IT and security posture (at a business level)</li>
      </ul>
      <h2 class="section-title" style="margin-top:10px">You receive:</h2>
      <p style="margin-top:10px">A prioritized 5–10 item Improvement Roadmap, each with:</p>
      <ul class="filled" style="margin-top:10px">
        <li>Business impact</li>
        <li>Relative effort</li>
        <li>ROI potential</li>
      </ul>
      <p class="gap">Price: $2,500<br>No upsell required. No obligation beyond the assessment.</p>
    </div>

    <div class="block on-navy" style="left:32px;top:1294px;width:400px">
      <h2 class="section-title">Who This Is For</h2>
      <ul class="box" style="margin-top:18px">
        <li>Small and mid-sized businesses</li>
        <li>Leadership teams feeling “tech pressure”<br>but lacking a plan</li>
        <li>Companies scaling headcount faster than systems</li>
        <li>Owners tired of guessing which tools to buy next</li>
      </ul>
    </div>

    <div class="block on-navy" style="left:558px;top:1294px;width:630px">
      <h2 class="section-title">Why Start Here</h2>
      <p style="margin-top:18px">Because buying more software without fixing workflows just adds complexity.<br>This assessment gives you:</p>
      <ul class="box" style="margin-top:6px">
        <li>Clarity instead of opinions</li>
        <li>A roadmap instead of random fixes</li>
        <li>Confidence before spending more money</li>
      </ul>
    </div>

    <div class="cta-lines">Start with insight. Move forward with confidence.<br>Let’s identify what’s actually holding your business back — and how to fix it.</div>
    <div class="cta-button">BOOK A TECHNOLOGY ENABLEMENT ASSESSMENT</div>
  </div>
</div>
</body>
</html>
```